Web Design Project

Company Name: Lumora Clinic & Skin Studio

Logo & Business Card Designs:
http://brightvanecreative.example/fileshare/lumora/Lumora_4xOptions_1.pdf
http://brightvanecreative.example/fileshare/lumora/Lumora-logo.jpg
http://brightvanecreative.example/fileshare/lumora/Lumora-logo.pdf

Colour scheme - As per logo above

Navigation: Top horizontal

Page structure (with drop-downs for sub-items) -
Home
The Practice
o Dr Vellacott
o Meet the Team
Surgical
o Breast Augmentation
o Breast Reduction
o Liposuction
o Abdominoplasty (Tummy Tuck)
o Rhinoplasty (Nose Reshaping)
o Face Lift
o Neck Lift
o Foreheadplasty (Brow Lift)
o Blepharoplasty (Eyelid Surgery)
o Arm Reduction
o Thigh Lift
o Otoplasty (Ear Pin Back)
o Fat Grafting/Fat Transfer
o Skin Cancer Surgery
Non-Surgical
o Anti-wrinkle Treatment
o Laser Skin Rejuvenation
o IPL
o Cologin Induction Treatment/Skin Needling
o Skin Peels
o Platelet Rich Plasma (PRP) Injections
Medi-Spa
o Crystal Microdermabration
o Superficial Skin Peels
o Vantir Skin Rejuvenation
o Laser Hair Removal
o Medical Micro Content
o Low Intensity Laser Therapy
o Facials
o Eye Brow Therapy
o Eye Lash Tints
Shop
Bookings
o Pricing
o Financing
o Appointments
FAQ’s
Media
Contact Us

Includes 3 'Featured Boxes' on the home page for: Breast Augmentation, Non-Surgical Procedures, Dr Vellacott

There will be a small shopping cart facility on the page, please include an icon/button for "Start Shopping"

Include an icon/button for 'Our Monthly Offer'

Include a 'search' field

Include an enquiry form the right hand panel including the following fields: Name, Email, Phone, Service Interested In (drop-down)

Please list the phone number in the top right corner of all pages - (03) 9555 0142

Footer:
Please include a Google Map icon like this site - http://www.ridgetowbarsupply.example/ with the following details-
and the following contact details:
58 Penrose Avenue
Kelwyn VIC 3199
Melbourne, Australia
Tel: (03) 9555 0142
Fax: (03) 9555 0187
Email: info@lumoraclinic.example

Websites they like - http://www.fernleighskin.example/

Some images to use from www.pixelharbourimages.example -

stock-illustration-30718452-medicine
stock-photo-8126054-natural-beauty
stock-photo-16347219-elegant-middle-aged-woman-with-her-arms-crossed-against-white
stock-photo-18273045-cellulite-body-and-beauty
stock-photo-31126408-laughing-man
stock-photo-31663127-our-practice-is-all-about-a-patient-s-protection
stock-photo-31852016-she-s-a-positive-and-caring-representative-of-her-profession
stock-photo-31922784-natural-beauty
stock-photo-31941698-healthy-young-fitness-woman-holding-waterbottle
stock-photo-31946286-happy-mature-woman
stock-photo-31951233-portrait-of-beautiful-girl
stock-photo-31951238-close-up-of-female-face-perfect-pure-skin
stock-photo-31951240-close-up-of-female-face-pure-skin-and-freckles
stock-photo-31951270-close-up-of-beautiful-female-face-beauty-portrait
stock-photo-31951523-beautiful-woman
stock-photo-31954463-passion-for-fruits
stock-photo-31954646-slices-of-fruit
stock-photo-31955436-beautiful-woman-enjoying-in-a-sunny-autumn-day
stock-photo-31955534-beautiful-couple-enjoying-in-autumn-day
stock-photo-31955549-beautiful-couple-rides-bikes-on-a-autumn-day
stock-photo-31956531-happy-mature-woman
stock-photo-31957652-beautiful-young-women
stock-photo-31958425-pretty-young-woman-with-cute-smile
stock-photo-31961832-healthy-elastic-skin
stock-photo-31962490-back-massage-at-spa
stock-photo-31963034-young-pensive-woman
stock-photo-31963585-relaxing-massage-at-spa
stock-photo-31963664-beautiful-young-pensive-woman
stock-photo-31964702-attractive-woman-having-botox-injections-in-face

```html
<!DOCTYPE html>
<html lang="en">
<head>
<meta charset="utf-8">
<title>Lumora Clinic &amp; Skin Studio</title>
<link rel="stylesheet" href="https://fonts.googleapis.com/css2?family=Ubuntu:wght@400;500;700&family=Arimo:wght@400;700&family=Comfortaa:wght@500;700&display=swap">
<style>
:root{
  --teal:#3e6e6b;
  --teal-dark:#2f5b58;
  --teal-light:#5c8f8b;
  --green:#7e9e60;
  --green-dark:#6a8a4e;
  --green-light:#9ab97c;
  --ink:#333;
  --grey:#666;
  --paper:#ffffff;
  --mist:#e4e4e4;
}
*{margin:0;padding:0;box-sizing:border-box}
html,body{width:1200px;height:1108px;overflow:hidden}
body{position:relative;background:var(--paper);font-family:"Arimo",Arial,sans-serif;color:var(--ink)}
.abs{position:absolute}
.header{left:0;top:0;width:1200px;height:112px;background:var(--teal)}
.brand{left:161px;top:30px;width:270px;color:#fff;font-family:"Ubuntu",sans-serif;font-weight:400;font-size:26px;line-height:28px;display:flex;align-items:center;gap:10px;white-space:nowrap}
.brand .dot{width:14px;height:14px;border-radius:50%;background:#fff;flex:none}
.brand.footer-brand{left:0;top:0;position:relative;width:auto}
.phone{left:872px;top:10px;color:#fff;font-family:"Ubuntu",sans-serif;font-size:24px;display:flex;align-items:center;gap:8px}
.search{left:828px;top:63px;width:224px;height:31px;border-radius:5px;background:var(--teal-dark);box-shadow:inset 0 1px 3px rgba(0,0,0,.35);color:#c9dcda;font-family:"Ubuntu",sans-serif;font-size:12px;line-height:31px;padding-left:8px}
.search .go{position:absolute;right:0;top:0;width:31px;height:31px;border-radius:0 5px 5px 0;background:linear-gradient(#e8e8e8,#b9b9b9);display:flex;align-items:center;justify-content:center}
.navband{left:0;top:112px}
.nav{left:0;top:117px;width:1200px;height:30px;font-family:"Ubuntu",sans-serif;font-size:13px;color:#fff;list-style:none}
.nav li{position:absolute;top:0;line-height:30px}
.nav .home{left:171px;top:2px;width:55px;height:25px;line-height:25px;text-align:center;border-radius:4px;background:var(--green-dark);box-shadow:inset 0 1px 3px rgba(0,0,0,.3)}
.nav .sep{width:1px;height:26px;top:2px;background:rgba(255,255,255,.3);box-shadow:1px 0 0 rgba(0,0,0,.12)}
.dropdown{left:434px;top:142px;width:177px;height:130px;background:rgba(70,110,105,.75);border-radius:0 0 4px 4px;padding:8px 8px;z-index:5}
.dropdown li{list-style:none;height:23px;margin-bottom:5px;border-radius:3px;background:rgba(140,180,110,.85);color:#fff;font-size:10px;line-height:23px;padding-left:26px;position:relative}
.dropdown li::before{content:"";position:absolute;left:13px;top:9px;border-left:4px solid #fff;border-top:3px solid transparent;border-bottom:3px solid transparent}
.stage{left:0;top:158px;width:1200px;height:306px;background:linear-gradient(#fff 0,#fff 40%,#dedede 100%)}
.hero{left:166px;top:187px;width:420px;height:240px;border-radius:8px;background:linear-gradient(#3d6d6a,#4c7e7b);box-shadow:0 10px 12px -6px rgba(0,0,0,.35)}
.hero h1{position:absolute;left:22px;top:18px;font-family:"Ubuntu",sans-serif;font-weight:700;font-size:26px;line-height:28px;color:#fff;letter-spacing:.5px}
.hero h1 em{font-style:normal;color:var(--green-light)}
.hero p{position:absolute;left:22px;top:86px;width:370px;font-size:10px;line-height:16.6px;color:#fff;text-align:justify}
.btn-more{left:400px;top:384px;width:142px;height:31px;border-radius:6px;background:linear-gradient(#fff,#dcdcdc);box-shadow:0 1px 3px rgba(0,0,0,.4);font-family:"Ubuntu",sans-serif;font-size:11px;color:#444;line-height:31px;padding-left:11px}
.btn-more span{font-size:16px;font-weight:700;margin-left:6px}
.hero-frame{left:574px;top:162px;width:430px;height:291px;background:#f2f2f2;border:1px solid #d0d0d0;padding:6px}
.hero-photo{width:100%;height:100%;background:linear-gradient(100deg,#c7d6de 0%,#6f96b4 35%,#e8a99a 55%,#8fb3c6 80%,#dfe8ee 100%)}
.feature{top:478px;height:159px;border-radius:3px;overflow:hidden;border:1px solid rgba(0,0,0,.2)}
.feature .photo{position:absolute;right:0;top:0;width:48%;height:100%}
.feature h2{position:absolute;left:11px;top:8px;font-family:"Ubuntu",sans-serif;font-weight:400;font-size:18px;white-space:nowrap}
.feature ul{position:absolute;left:8px;top:43px;list-style:none;font-size:10px;line-height:16.6px}
.feature li::before{content:"»";font-weight:700;margin-right:3px}
.feature .shop{position:absolute;left:8px;top:131px;height:20px;padding:0 9px;border-radius:3px;font-family:"Ubuntu",sans-serif;font-size:10px;line-height:20px}
.f1{left:166px;width:287px;background:linear-gradient(#3f7471,#5e908c);color:#fff}
.f1 .photo{background:linear-gradient(90deg,rgba(94,144,140,0),#c9968a 40%,#e8ddd6 100%)}
.f2{left:458px;width:283px;background:linear-gradient(#f0f0f4,#d8d9e3);color:#333}
.f2 .photo{background:linear-gradient(90deg,rgba(230,230,236,0),#e6cfc2 40%,#3a5fa6 80%,#d5d9e6 100%)}
.f3{left:748px;width:283px;background:linear-gradient(#5e8454,#6a9a55);color:#fff}
.f3 .photo{background:linear-gradient(90deg,rgba(106,154,85,0),#d8b7a2 45%,#2c2e36 75%,#6a9a55 100%)}
.shop.light{background:linear-gradient(#fff,#d9d9d9);color:#333}
.shop.dark{background:linear-gradient(#555,#222);color:#fff;font-style:italic}
.article{left:174px;top:662px;width:566px}
.article h2{font-family:"Arimo",sans-serif;font-weight:400;font-size:17px;color:var(--teal);margin-bottom:10px}
.article p{font-size:10px;line-height:16.6px;color:#333;margin-bottom:16.6px}
.btn-read{left:652px;top:832px;width:80px;height:22px;border-radius:3px;background:var(--teal);border:2px solid #cfe0de;box-shadow:0 0 0 1px var(--teal);color:#fff;font-size:11px;line-height:18px;text-align:center}
.divider{left:746px;top:655px;width:2px;height:215px;background:linear-gradient(rgba(0,0,0,0),#ddd 30%,#ddd 70%,rgba(0,0,0,0))}
.enquiry{left:780px;top:662px;width:226px}
.enquiry h3{font-family:"Comfortaa",sans-serif;font-weight:700;font-size:17px;color:var(--teal);margin-bottom:12px}
.field{display:flex;align-items:center;justify-content:flex-end;height:21px;margin-bottom:8.5px;font-size:11.5px;color:#555}
.field span{margin-right:10px}
.field i{width:160px;height:21px;border-radius:11px;background:linear-gradient(#ddd,#f3f3f3);box-shadow:inset 0 1px 2px rgba(0,0,0,.15)}
.btn-free{left:877px;top:829px;width:129px;height:25px;border-radius:13px;background:linear-gradient(#6ea6a1,#3e6e6b);color:#fff;font-family:"Comfortaa",sans-serif;font-weight:700;font-size:12px;line-height:25px;text-align:center}
.footer{left:0;top:892px;width:1200px;height:216px;background:linear-gradient(#e6e6e6,#f7f7f7 40%,#e9e9e9)}
.footer-logo{left:161px;top:922px;width:275px;height:94px;background:var(--teal-light);border:1px solid #4a7a76;padding:18px 14px;overflow:hidden}
.mission{left:494px;top:907px;width:290px}
.mission h4,.location h4{font-family:"Ubuntu",sans-serif;font-weight:500;font-size:18px;color:#666;letter-spacing:.4px;margin-bottom:12px}
.mission p{font-size:10px;line-height:16.6px;color:#555;margin-left:-2px}
.q{font-family:Georgia,serif;font-size:34px;color:#999;font-weight:700}
.location{left:865px;top:900px}
.map{left:863px;top:930px;width:160px;height:97px;border:1px solid #ccc;background:linear-gradient(135deg,#e9e3d2,#f2e79a 50%,#d9d5c8)}
.baseband{left:0;top:1038px}
.credits{left:0;top:1060px;width:1200px;text-align:center;color:#fff;font-size:10px;line-height:22px}
</style>
</head>
<body>

<header class="abs header"></header>
<div class="abs brand"><span class="dot"></span><span>Lumora Clinic<br>&amp; Skin Studio</span></div>
<div class="abs phone">
  <svg width="28" height="28" viewBox="0 0 28 28" aria-hidden="true"><path d="M8 4h9a2 2 0 0 1 2 2v16a2 2 0 0 1-2 2H8a2 2 0 0 1-2-2V6a2 2 0 0 1 2-2z" fill="none" stroke="#fff" stroke-width="2" transform="rotate(25 13 14)"/><path d="M19 3a6 6 0 0 1 5 5M20 0a9 9 0 0 1 7 7" fill="none" stroke="#fff" stroke-width="1.6"/></svg>
  <span>(03) 9555 0142</span>
</div>
<div class="abs search">Site Search
  <div class="go"><svg width="16" height="16" viewBox="0 0 16 16" aria-hidden="true"><circle cx="6.5" cy="6.5" r="4.5" fill="none" stroke="#333" stroke-width="2"/><path d="M10 10l5 5" stroke="#333" stroke-width="3"/></svg></div>
</div>

<div class="abs stage"></div>
<svg class="abs navband" width="1200" height="50" viewBox="0 0 1200 50" aria-hidden="true">
  <defs><linearGradient id="nb" x1="0" y1="0" x2="0" y2="1"><stop offset="0" stop-color="#8aab6b"/><stop offset="1" stop-color="#6d8f51"/></linearGradient></defs>
  <path d="M0 0H1200V47Q600 30 0 47Z" fill="url(#nb)"/>
</svg>
<ul class="abs nav">
  <li class="home">Home</li>
  <li class="sep" style="left:236px"></li><li style="left:252px">The Practice</li>
  <li class="sep" style="left:337px"></li><li style="left:356px">Surgical</li>
  <li class="sep" style="left:420px"></li><li style="left:438px">Non-Surgical</li>
  <li class="sep" style="left:531px"></li><li style="left:546px">Medi-Spa</li>
  <li class="sep" style="left:616px"></li><li style="left:636px">Shop</li>
  <li class="sep" style="left:681px"></li><li style="left:703px">Bookings</li>
  <li class="sep" style="left:771px"></li><li style="left:792px">FAQ’s</li>
  <li class="sep" style="left:841px"></li><li style="left:860px">Media</li>
  <li class="sep" style="left:914px"></li><li style="left:932px">Contact Us</li>
</ul>
<ul class="abs dropdown">
  <li>Anti-wrinkle Treatment</li>
  <li>Laser Skin Rejuvenation</li>
  <li>IPL</li>
  <li>Skin Peels</li>
</ul>

<section class="abs hero">
  <h1>Toenail Know-how <em>Surgery</em><br><em>Without a drop</em> of blood</h1>
  <p>Lorem Ipsum is simply dummy text of the printing and typesetting industry. Lorem Ipsum has been the industry's standard dummy text ever since the 1500s, when anthe industry's standard dummy text ever since the 1500s, when an unknown printer took a galley of type and scrambled it to make a type specimen book. It has survived not only five centuries, but also the leap</p>
</section>
<div class="abs btn-more">MORE INFORMATION<span>››</span></div>
<div class="abs hero-frame"><div class="hero-photo" role="img" aria-label="Smiling young woman in a coral top in front of a surgical team"></div></div>

<article class="abs feature f1">
  <div class="photo" role="img" aria-label="Nurse in red scrubs caring for a patient"></div>
  <h2>Breast Augmentation</h2>
  <ul><li>Nemo ipsam voluptatem</li><li>Nemo enim voluptatem</li><li>Nemo ipsam voluptatem</li><li>Nemo in voluptatem</li><li>Nemo enim &nbsp;voluptatem</li></ul>
  <div class="shop light">Shopping Now</div>
</article>
<article class="abs feature f2">
  <div class="photo" role="img" aria-label="Smiling nurse holding a clipboard"></div>
  <h2>Non-Surgical Procedures</h2>
  <ul><li>Nemo ipsam voluptatem</li><li>Nemo enim voluptatem</li><li>Nemo ipsam voluptatem</li><li>Nemo &nbsp;em enim voluptatem</li><li>Nemo enim &nbsp;voluptatem</li></ul>
  <div class="shop dark">Shopping Now</div>
</article>
<article class="abs feature f3">
  <div class="photo" role="img" aria-label="Portrait of the doctor in a dark suit"></div>
  <h2>Dr Vellacott</h2>
  <ul><li>Nemo ipsam voluptatem</li><li>Nemo enim voluptatem</li><li>Nemo ipsam voluptatem</li><li>Nemo &nbsp;em enim voluptatem</li><li>Nemo enim &nbsp;voluptatem</li></ul>
  <div class="shop light">Shopping Now</div>
</article>

<section class="abs article">
  <h2>Marlow College in Westbrook, looked up one of the more obscure</h2>
  <p><b>simply dummy text of the printing</b> and typesetting industry. Lorem Ipsum has been the industry's standard dummy text ever since the 1500s, when an unknown printer took a galley of type and scrambled it to make a type specimen book.</p>
  <p>It has survivedunknown <b>printer took a galley</b> of type and scrambled it to make a type specimen book. It has survived an unknown printer took a galley of type and scrambled it to make a type specimen book. It has survived not only five centuries, but also the leap into electronic typesetting, remaining essentially unchanged. It was popularised in the 1960s with the release of Letraset sheets containing</p>
</section>
<div class="abs btn-read">READ MORE</div>
<div class="abs divider"></div>

<form class="abs enquiry">
  <h3>Free Consultations</h3>
  <div class="field"><span>Name:*</span><i></i></div>
  <div class="field"><span>Email:*</span><i></i></div>
  <div class="field"><span>Phone:*</span><i></i></div>
  <div class="field"><span>Message:*</span><i></i></div>
</form>
<div class="abs btn-free">Free Consultations</div>

<footer class="abs footer"></footer>
<div class="abs footer-logo"><div class="brand footer-brand"><span class="dot"></span><span>Lumora Clinic<br>&amp; Skin Studio</span></div></div>
<section class="abs mission">
  <h4>Our Mission</h4>
  <div style="display:flex;gap:4px">
    <span class="q" style="line-height:30px;margin-left:-24px">“</span>
    <p>Our primary concern is the welfare of our patients and the effectiveness, safety and appropriateness of the treatments we and appropriateness of the treatments we provide. standards and give you the right advice, quality care and successful outcomes.</p>
  </div>
  <div class="q" style="position:absolute;left:266px;top:112px;line-height:30px">”</div>
</section>
<section class="abs location"><h4>Location</h4></section>
<div class="abs map" role="img" aria-label="Street map showing the clinic location"></div>

<svg class="abs baseband" width="1200" height="70" viewBox="0 0 1200 70" aria-hidden="true">
  <path d="M0 20Q600 -8 1200 20V70H0Z" fill="#3e6e6b"/>
</svg>
<div class="abs credits">© Copyright 2012 Lumora Clinic &amp; Skin Studio (use copyright symbol)<br>Website &amp; Search Engine Optimisation by BrightvaneCreative</div>

</body>
</html>
```